Modern Business Card for Industrial Company

We need business cards updated with modern fonts and make it look more technical, sharp and clean. The logo should not be changed, but we are looking for fresh solutions for how other information on the card is laid out in an interesting way. The company provides machinery and services to the ceramic industry and deals with cutting-edge technology. The design should reflect a technologically advanced and modern company that deals with the latest European technologies.

Font styles to use
Sans Serif

Requirements
Must have
• Modern fonts, technical look and feel

```html
<!DOCTYPE html>
<html lang="en">
<head>
<meta charset="utf-8">
<title>Norvia Tech — Business Card</title>
<link href="https://fonts.googleapis.com/css2?family=Michroma&display=swap" rel="stylesheet">
<style>
  :root{
    --brand-blue:#0d4f96;
    --brand-blue-deep:#0b3f7a;
    --accent-red:#c8232c;
    --steel-grey:#a7abb1;
    --paper:#ffffff;
    --backdrop:#2b2b2d;
  }
  *{box-sizing:border-box;margin:0;padding:0}
  html,body{width:1200px;height:900px;overflow:hidden}
  body{background:var(--backdrop);font-family:"Michroma",sans-serif;position:relative}

  .card{position:absolute;left:320px;width:560px;height:320px;border-radius:18px;overflow:hidden;box-shadow:0 10px 30px rgba(0,0,0,.45)}
  .card--back{top:100px;background:var(--brand-blue)}
  .card--front{top:470px;background:var(--paper)}

  .back-pattern{position:absolute;inset:0;background:linear-gradient(120deg,var(--brand-blue-deep) 0%,var(--brand-blue) 55%,#1560ad 100%)}
  .back-name{position:absolute;right:56px;top:135px;color:var(--paper);font-size:26px;letter-spacing:1px}

  .card-shapes{position:absolute;inset:0}

  .company-name{position:absolute;left:40px;top:96px;display:flex;align-items:center;gap:14px;color:var(--brand-blue);font-size:34px;letter-spacing:1px;line-height:1}
  .company-name .mark{width:20px;height:20px;background:var(--brand-blue)}

  .person-name{position:absolute;left:330px;top:44px;color:var(--paper);font-size:15px;letter-spacing:1px;line-height:1.4}
  .person-role{position:absolute;left:404px;top:72px;color:var(--accent-red);font-size:12px;letter-spacing:1px;line-height:1.4}

  .address{position:absolute;right:56px;top:178px;text-align:right;color:var(--brand-blue);font-size:11px;line-height:1.7;letter-spacing:.5px;font-style:normal}
  .address .pin{position:absolute;right:-28px;top:2px}

  .contact-list{position:absolute;left:40px;top:222px;list-style:none;color:var(--brand-blue);font-size:11.5px;letter-spacing:.5px}
  .contact-list li{display:flex;align-items:center;gap:12px;height:24px;white-space:nowrap}
  .icon-tile{width:17px;height:17px;background:var(--accent-red);border-radius:3px;display:flex;align-items:center;justify-content:center;flex:none}
</style>
</head>
<body>

<section class="card card--back" aria-label="Card back">
  <div class="back-pattern" role="img" aria-label="Repeating company mark pattern in tonal blue"></div>
  <p class="back-name">Norvia Tech</p>
</section>

<section class="card card--front" aria-label="Card front">
  <svg class="card-shapes" viewBox="0 0 560 320" width="560" height="320" aria-hidden="true">
    <polygon points="268,36 560,36 560,66 300,66" fill="var(--brand-blue)"/>
    <polygon points="250,52 282,52 296,66 264,66" fill="var(--accent-red)"/>
    <rect x="0" y="206" width="280" height="3" fill="var(--brand-blue)"/>
    <rect x="280" y="166" width="280" height="3" fill="var(--accent-red)"/>
    <polygon points="0,300 470,300 490,320 0,320" fill="var(--brand-blue)"/>
    <polygon points="470,300 560,300 560,320 490,320" fill="var(--steel-grey)"/>
  </svg>

  <div class="company-name"><span class="mark"></span>Norvia Tech</div>

  <p class="person-name">MARCO BELLINI</p>
  <p class="person-role">PRESIDENT</p>

  <address class="address">
    480 HALDEN ROAD, SUITE 200<br>BROOKFIELD, WI 53005
    <span class="pin icon-tile">
      <svg width="10" height="12" viewBox="0 0 10 12"><path d="M5 0a4 4 0 0 0-4 4c0 3 4 8 4 8s4-5 4-8a4 4 0 0 0-4-4z" fill="#fff"/><circle cx="5" cy="4" r="1.5" fill="var(--accent-red)"/></svg>
    </span>
  </address>

  <ul class="contact-list">
    <li><span class="icon-tile"><svg width="10" height="10" viewBox="0 0 10 10"><path d="M2 0.5l2 2-1 1.2a6 6 0 0 0 3.3 3.3l1.2-1 2 2-1.3 1.5C4.5 9.5 0.5 5.5 0.5 1.8z" fill="#fff"/></svg></span>555-014-2290</li>
    <li><span class="icon-tile"><svg width="11" height="8" viewBox="0 0 11 8"><rect x="0.5" y="0.5" width="10" height="7" fill="none" stroke="#fff"/><path d="M0.5 0.5l5 4 5-4" fill="none" stroke="#fff"/></svg></span>MBELLINI@NORVIATECH.COM</li>
    <li><span class="icon-tile"><svg width="11" height="11" viewBox="0 0 11 11"><circle cx="5.5" cy="5.5" r="4.8" fill="none" stroke="#fff"/><ellipse cx="5.5" cy="5.5" rx="2" ry="4.8" fill="none" stroke="#fff"/><path d="M0.7 5.5h9.6" stroke="#fff"/></svg></span>WWW.NORVIATECH.COM</li>
  </ul>
</section>

</body>
</html>
```